Organic Mushroom company needs shipping box design

Hello! Thanks for helping us out.

We need help creating a shipping box design for our product. This is our first product with many more to come so the designer that provides the best design has the potential to be picked for all of those other product packaging designs too!

Our product is a at home mushroom growing kit. Which allows our customers to grow their own mushrooms within their own home straight out of the box or having to take them out.

Here are some examples of other companies doing it:

(example 1) https://fernvalecrate.com/collections/mushroom-grow-kits/products/mushroom-grow-kit
(example 2:) https://quillmoss.com/pages/growkits

Packaging Box Style: I added the box dimensions in a file and also a visual image of what our product looks like inside of the box. The box is a shipping box.

Logo: I added the logo in the files

Product Information: We will be using the same box for 2 different products (shiitake mushroom growing kit and oyster mushroom growing kit) so we want something that can be used for both. I added photos of examples of what the actual product looks like inside and outside of the shipping box.

Theme: We want our customers to feel like we are bringing a miniature garden to their homes since these kits will be used inside their house. So the goal is to make the box look like a center piece or attractive to the eye when looked at.

The OUTSIDE OF THE BOX can be very simple. We want just our logo on the top and on the outside panels to look similar to a wooden box or miniature garden fence.

The INSIDE OF THE BOX we are open to different ideas but our idea was that on the back panel we have somewhat of a garden or green like design that will be a good/photogenic back drop for once the mushrooms start to grow ( i added a photo that shows what it would look like once they start to grow and also added an example of what the garden backdrop could look like).

Colors: Using the colors from the logo will help and we since we want to go with a clean garden feel - I would say colors like green, white, wood, tan , etc.

The box will remain open the entire time once the customer receives it so we want the inside to be as pleasing to the eye as possible

Let me know if you have any questions or need additional information ! Thank you so much!

Blank Width: 37+7/16 x 32 1/8
Finished Size: 17 x 9 x 4 1/2

Target Market(s)

Home gardening, organic lovers, DIY kits, farming

Font styles to use
Serif

Colors
9bcb3c
abd037
cadf82
fdfad7
fefdec
ffffff
f6faec

Requirements
Must have
• Must contain the Mushroom Lark logo.

The outer portion of the box should be simple since it will be shipped out like this, but the inside is the most important.

3 colors on the outside layer
3 colors on the inside layer
Nice to have
• We want our customers to feel like we are bringing a miniature garden to their homes since these kits will be used inside their house. So the goal is to make the box look like a center piece or attractive to the eye when looked at.

The box will remain open when they are growing the mushrooms so the inside of the box is more important than the outside.

When they open the box we prefer it to be green and have a garden like feel. For example, when they open it the backdrop should be some sort of garden with leaves, woods, or plant design so once the mushrooms start growing in the box then it will look like it's growing outside in a real garden or in nature.

The outside layer could be a wooden fence (gardening fence) so that it represents a mini garden.
Should not have
• We are limited to only 3 colors on each side. These are the limits of the box printer that we are working with. Please do not use more than 3 colors on each side.

```html
<!DOCTYPE html>
<html lang="en">
<head>
<meta charset="utf-8">
<title>Home Grown Mushroom Kit – Shipping Box</title>
<link rel="stylesheet" href="https://fonts.googleapis.com/css2?family=Bebas+Neue&family=Poppins:wght@500&display=swap">
<style>
  :root {
    --backdrop: #e2d3a9;
    --kraft: #c9a57c;
    --kraft-edge: #b78f63;
    --wood-dark: #5a3822;
    --wood-mid: #7a4e2f;
    --band-green: #6fa02d;
    --band-green-deep: #5f8f25;
    --ink: #1e2411;
    --sketch: #e7d2a8;
  }
  * { margin: 0; padding: 0; box-sizing: border-box; }
  html, body { width: 1200px; height: 849px; overflow: hidden; }
  body {
    background: var(--backdrop);
    display: flex;
    align-items: center;
    justify-content: center;
  }
  .box-layout {
    position: relative;
    width: 720px;
    height: 740px;
  }
  .panel-top {
    position: absolute;
    left: 0; top: 0;
    width: 720px; height: 460px;
    background: var(--kraft);
    border: 2px solid var(--kraft-edge);
  }
  .panel-front {
    position: absolute;
    left: 0; top: 460px;
    width: 720px; height: 280px;
    background: linear-gradient(180deg, var(--wood-mid), var(--wood-dark));
    border: 2px solid var(--wood-dark);
  }
  .band {
    position: absolute;
    left: 220px;
    width: 270px;
    background: linear-gradient(160deg, var(--band-green), var(--band-green-deep));
  }
  .band--top { top: 0; height: 460px; padding: 44px 26px 0; }
  .band--front { top: 460px; height: 280px; display: flex; align-items: center; justify-content: center; }
  .kit-title {
    font-family: "Bebas Neue", sans-serif;
    font-size: 50px;
    line-height: 0.95;
    letter-spacing: 2px;
    color: var(--ink);
  }
  .title-rule {
    height: 2px;
    background: var(--ink);
    margin: 12px 0 12px;
  }
  .kit-tagline {
    font-family: "Poppins", sans-serif;
    font-weight: 500;
    font-size: 19px;
    line-height: 1.25;
    color: var(--ink);
  }
  .mushroom-art {
    width: 150px;
    height: 130px;
    border-radius: 50% 50% 30% 30%;
    background: radial-gradient(circle at 50% 40%, var(--sketch) 0%, rgba(231,210,168,0.35) 70%);
    opacity: 0.7;
  }
  .band--top .mushroom-art { margin: 34px 0 0 70px; }
</style>
</head>
<body>
  <main class="box-layout">
    <section class="panel-top" aria-label="Box lid"></section>
    <section class="panel-front" role="img" aria-label="Wood grain fence texture"></section>

    <div class="band band--top">
      <h1 class="kit-title">Home Grown<br>Mushroom Kit</h1>
      <div class="title-rule"></div>
      <p class="kit-tagline">Grow your mushroom<br>at your home</p>
      <div class="mushroom-art" role="img" aria-label="Line sketch of a mushroom"></div>
    </div>

    <div class="band band--front">
      <div class="mushroom-art" role="img" aria-label="Line sketch of a mushroom"></div>
    </div>
  </main>
</body>
</html>
```